Tallow Roast Coffee Packaging Design

I am looking to design packaging for a coffee brand I am creating. I own a cigar lounge and would like to design a logo and package design that reflects my coffee that will pair well with our cigars. The name of the brand is "Tallow Roast". I have a template for the packaging I will upload and I also have some coffee packages that I like to give inspiration. I did have one created recently that I sort of liked but have decided to not use our logo from the Cigar lounge. I am trying to make the establishment look more "classy" so I will not be using the "girl riding a cigar" on the coffee brand as shown in the design I uploaded. I am undecided on colors although our company utilizes mostly Black, Red, Gold in our Logo. I like the style of the Amber Finch logo I uploaded as well. I am open to any design ideas so I feel a contest may be the best way to get multiple variations to choose from.

Target Market(s)

Cigar smokers that drink coffee

Industry/Entity Type

Coffee Company

Requirements
Must have
• The template design must include what the packaging will look like when printed
Nice to have
• I included an Illustrator file to get the current "Tallow Roast" logo from
Should not have
• The girl must be removed and I'm looking for ideas to replace it with something more "classy."

```html
<!DOCTYPE html>
<html lang="en">
<head>
<meta charset="utf-8">
<title>Tallow Roast – Cinder Kiss Packaging</title>
<link href="https://fonts.googleapis.com/css2?family=Alfa+Slab+One&family=Arvo:wght@400;700&family=Barlow:wght@500;700&display=swap" rel="stylesheet">
<style>
:root{
  --cream:#fcefdc;
  --paper:#fbe6c4;
  --orange:#e8522c;
  --ink:#231c1a;
  --sepia:#6b4a33;
  --gold:#c9a25b;
  --wood:#8a6a52;
  --white:#ffffff;
  --grey:#555;
  --magenta:#e0218a;
  --green:#3fae5a;
  --yellow:#f4ea1a;
}
*{margin:0;padding:0;box-sizing:border-box}
html,body{width:1200px;height:2701px;overflow:hidden;background:var(--cream)}
body{position:relative;font-family:"Arvo",serif;color:var(--ink)}
.abs{position:absolute}

/* brand mark */
.brandmark{display:flex;align-items:center;gap:12px;color:var(--orange);font-family:"Alfa Slab One",serif;line-height:.95;text-align:center}
.brandmark .ring{border:5px solid var(--orange);border-radius:50%}

.hero-mark{left:0;top:0;width:1200px;height:315px;justify-content:center;font-size:44px}
.hero-mark .ring{width:60px;height:60px}

/* flat bag front */
.bag-front{left:0;top:315px;width:501px;height:1049px;background:var(--paper);overflow:hidden}
.illustration{background:linear-gradient(160deg,rgba(107,74,51,.35) 0%,rgba(251,230,196,0) 30%,rgba(107,74,51,.55) 55%,rgba(35,28,26,.9) 85%)}
.mockup{left:501px;top:315px;width:699px;height:1049px;background:linear-gradient(135deg,#9b7a60,#6e523f 55%,#8d6d55)}

.label{background:var(--white);border-radius:120px 120px 0 0;text-align:center;display:flex;flex-direction:column;align-items:center}
.label .seal{width:62px;height:62px;border:4px solid var(--orange);border-radius:50%;margin-top:34px}
.label h2{font-family:"Alfa Slab One",serif;color:var(--orange);font-weight:400;font-size:29px;line-height:1;margin-top:12px;letter-spacing:.5px}
.label .desc{font-size:9px;font-weight:700;line-height:1.15;margin-top:18px;width:160px}
.label .specs{width:200px;margin-top:18px;font-size:8px;font-weight:700}
.label .specs div{border-top:1px solid var(--ink);padding:3px 0}
.label .specs div:first-child{border-top:none;border-bottom:1px solid var(--ink)}
.label .specs .by{border-top:1px solid var(--ink);display:flex;justify-content:space-between}
.label .bar{background:var(--orange);width:100%;margin-top:auto}

/* dieline */
.dieline{left:0;top:1424px;width:1200px;height:1235px;background:var(--paper);border-top:3px solid var(--yellow);border-bottom:3px solid var(--yellow)}
.back-panel{left:5px;top:0;width:342px;height:1229px;background:var(--ink);color:var(--paper)}
.panel-title{font-family:"Barlow",sans-serif;font-weight:700;font-size:44px;text-align:center;line-height:1;color:var(--ink)}
.panel-dim{font-family:"Barlow",sans-serif;font-weight:700;font-size:15px;text-align:center;color:var(--ink)}
.back-panel .panel-dim{color:#5a504b;font-weight:500}
.tin-tie{left:0;top:99px;width:342px;height:26px;background:#000;color:var(--white);font-family:"Barlow",sans-serif;font-weight:700;font-size:8px;text-align:center;line-height:26px}
.partner{left:37px;top:275px;width:269px;justify-content:center;color:var(--gold);font-family:"Alfa Slab One",serif;font-size:30px}
.partner .ring{width:48px;height:48px;border:3px solid var(--gold);border-radius:50%}
.back-copy{left:68px;top:398px;width:212px;font-family:"Alfa Slab One",serif;font-size:11.5px;line-height:.83;text-align:center;color:var(--paper)}
.back-copy p+p{margin-top:14px}
.fine{font-family:"Barlow",sans-serif;font-size:7px;line-height:1.25;color:#6a5d55;text-transform:uppercase}
.guide-v{width:1px;background:var(--magenta)}
.safe{border:1px solid var(--green)}
.fold{left:0;top:1043px;width:1200px;height:1px;background:#7a4a3a}
.dim-line{height:1px;background:#777}
.valve{width:70px;height:70px;border:3px solid #cfc5b6;border-radius:50%;font-family:"Barlow",sans-serif;font-weight:700;font-size:12px;display:flex;align-items:center;justify-content:center;color:#333}
.swatch{width:24px;height:22px}
.vert-note{left:1120px;top:590px;width:700px;transform:rotate(-90deg);transform-origin:0 0;font-family:"Barlow",sans-serif;font-weight:700;font-size:11px;color:#e6d2b3;line-height:1.4;text-align:center}
</style>
</head>
<body>

<div class="abs brandmark hero-mark"><span class="ring"></span><span>TALLOW<br>ROAST</span></div>

<section class="abs bag-front">
  <div class="abs illustration" style="left:0;top:0;width:501px;height:1049px" role="img" aria-label="Sepia engraving-style illustration of a gentleman in a pinstripe suit and bow tie smoking a cigar, with curling smoke"></div>
  <div class="abs brandmark" style="left:168px;top:90px;font-size:22px;gap:8px"><span class="ring" style="width:30px;height:30px;border-width:3px"></span><span>TALLOW<br>ROAST</span></div>
  <div class="abs label" style="left:131px;top:697px;width:238px;height:352px">
    <span class="seal"></span>
    <h2>CINDER<br>KISS</h2>
    <p class="desc">A fiery dark roast with a hint of bourbon evoking the volcanic mountains of Nicaragua.</p>
    <div class="specs">
      <div>WHOLE BEAN &nbsp;&nbsp;&nbsp;&nbsp; __ GROUND</div>
      <div>Flavor: Bourbon, Chocolate, Citrus</div>
      <div>Acidity: ☐ Medium Roast &nbsp; ☐ Light Roast<br>☐ Dark Roast</div>
      <div class="by"><span>By: Tallow Roast Coffee Co.</span><span>Net Wt: 12oz</span></div>
    </div>
    <div class="bar" style="height:21px;margin-top:10px"></div>
  </div>
</section>

<div class="abs mockup" role="img" aria-label="Product photo of the coffee bag lying on a wooden table"></div>

<section class="abs dieline">
  <div class="abs illustration" style="left:535px;top:8px;width:483px;height:928px" role="img" aria-label="Sepia engraving-style illustration of a gentleman smoking a cigar, with curling smoke"></div>

  <div class="abs back-panel">
    <div class="abs panel-title" style="left:0;top:24px;width:342px">BACK</div>
    <div class="abs panel-dim" style="left:0;top:66px;width:342px">3.6125”</div>
    <div class="abs tin-tie">TIN TIE (FOR PLACEMENT ONLY)</div>
    <div class="abs brandmark partner"><span class="ring"></span><span>AMBER FINCH</span></div>
    <div class="abs back-copy">
      <p>Lorem ipsum dolor sit amet, consectetur adipiscing elit. Aenean maximus dui nec semper consequat. Maecenas nisi ex, auctor vel fermentum a, laoreet ut lacus. Ut aliquet eros odio, vitae luctus nisi ullamcorper quis. Proin vulputate nec sem et viverra. Suspendisse dictum dui quis elit convallis tempus. Morbi aliquam massa ut turpis cursus, id pulvinar massa lobortis. Nullam scelerisque lorem tristique, aliquet risus a, consectetur eros. Curabitur porta quis justo vitae commodo. Aenean a consequat urna. Sed maximus nisi ac ante ultrices posuere.</p>
      <p>Cras aliquet non leo at semper. Class aptent taciti sociosqu ad litora torquent per conubia nostra, per inceptos himenaeos. Nunc sed mi sollicitudin, ultrices quam id, fermentum nisi. Ut eleifend dolor purus, a ornare ipsum imperdiet ut. Pellentesque enim sem, rutrum dignissim metus id, bibendum ultrices nunc. Aenean vitae semper magna. In tellus diam, ultrices at dignissim non, pharetra lobortis metus. Nam pretium quam sem. Aenean auctor massa at nisi facilisis, id ornare lorem hendrerit. Mauris sed hendrerit lectus. Curabitur eget ultrices erat. Integer sollicitudin magna ut ipsum pulvinar, accumsan tristique massa tincidunt. Morbi aliquam nibh ut lorem ultricies, et vehicula metus venenatis. Nunc non molestie lectus, sit amet finibus mi. Etiam sodales</p>
    </div>
    <div class="abs" style="left:0;top:1163px;width:37px;height:22px;background:var(--white)"></div>
    <div class="abs" style="left:0;top:1185px;width:37px;height:22px;background:#000;outline:1px solid var(--white)"></div>
    <div class="abs" style="left:0;top:1207px;width:37px;height:22px;background:var(--white)"></div>
    <p class="abs fine" style="left:63px;top:1186px;width:170px">This black and white graphic is the eyemark and will print in this location on the artwork.</p>
  </div>

  <div class="abs guide-v" style="left:347px;top:0;height:1229px"></div>
  <div class="abs guide-v" style="left:580px;top:0;height:1229px"></div>
  <div class="abs guide-v" style="left:928px;top:0;height:1229px"></div>
  <div class="abs safe" style="left:360px;top:19px;width:209px;height:1004px"></div>
  <div class="abs safe" style="left:599px;top:19px;width:310px;height:1132px"></div>
  <div class="abs safe" style="left:940px;top:19px;width:210px;height:1004px"></div>
  <div class="abs fold"></div>

  <div class="abs dim-line" style="left:348px;top:79px;width:852px"></div>
  <div class="abs panel-title" style="left:348px;top:24px;width:232px">SIDE</div>
  <div class="abs panel-dim" style="left:425px;top:69px;width:80px;background:var(--paper)">2.43”</div>
  <div class="abs panel-title" style="left:580px;top:24px;width:348px">FRONT</div>
  <div class="abs panel-dim" style="left:714px;top:69px;width:80px">3.625”</div>
  <div class="abs panel-title" style="left:928px;top:24px;width:232px">SIDE</div>
  <div class="abs panel-dim" style="left:1004px;top:69px;width:80px;background:var(--paper)">2.4572”</div>
  <div class="abs fine" style="left:1166px;top:73px;font-weight:700;color:#333">.3553”</div>

  <div class="abs brandmark" style="left:660px;top:106px;width:190px;justify-content:center;font-size:26px;gap:8px"><span class="ring" style="width:34px;height:34px;border-width:4px"></span><span>TALLOW<br>ROAST</span></div>
  <div class="abs valve" style="left:720px;top:241px">VALVE</div>

  <div class="abs label" style="left:637px;top:692px;width:237px;height:537px">
    <span class="seal"></span>
    <h2>CINDER<br>KISS</h2>
    <p class="desc">A fiery dark roast with a hint of bourbon evoking the volcanic mountains of Nicaragua.</p>
    <div class="specs">
      <div>☐ WHOLE BEAN &nbsp;&nbsp;&nbsp; ☐ GROUND</div>
      <div>Flavor: Bourbon, Chocolate, Citrus</div>
      <div>Acidity: ☐ Medium Roast &nbsp; ☐ Light Roast<br>☐ Dark Roast</div>
      <div class="by"><span>By: Tallow Roast Coffee Co.</span><span>Net Wt: 12oz</span></div>
    </div>
    <div class="bar" style="height:205px"></div>
  </div>

  <div class="abs" style="left:997px;top:1118px;display:grid;grid-template-columns:repeat(4,24px);gap:0">
    <span class="swatch" style="background:#00a3e0"></span><span class="swatch" style="background:#e4007c"></span><span class="swatch" style="background:#ffec00"></span><span class="swatch" style="background:#111"></span>
    <span class="swatch" style="background:#7fd0ef"></span><span class="swatch" style="background:#f07fbd"></span><span class="swatch" style="background:#fff27f"></span><span class="swatch" style="background:#999"></span>
    <span class="swatch" style="background:#cdeefa"></span><span class="swatch" style="background:#fbd0e6"></span><span class="swatch" style="background:#fffacd"></span><span class="swatch" style="background:#ddd"></span>
  </div>
  <p class="abs fine" style="left:955px;top:1191px;width:180px;text-align:center;color:#333;font-weight:700">To maintain color consistency, this color bar graphic will print in this location on the artwork.</p>
  <p class="abs vert-note">This area gets covered by the fin seal<br>We still recommend extending any color or background image from the side panel into this area</p>
</section>

</body>
</html>
```